Onlineshop für hochwertige Gebrauchtsättel für den Reitsport sucht Webdesign
Zielgruppe
Wir verkaufen hochwertige Gebrauchtsättel für den Reitsport und möchten Reiter jeder Altersgruppe ansprechen.
Aufgabenstellung
Farbgebung : grün braun (eventuell gelb), naturnahe Farben
Ein Logo ist bereits vorhanden.

```html
<!DOCTYPE html>
<html lang="de">
<head>
<meta charset="utf-8">
<title>Oakrein Sättel – Webdesign</title>
<link rel="stylesheet" href="https://fonts.googleapis.com/css2?family=Open+Sans:wght@400;700&family=PT+Sans:wght@400;700&display=swap">
<style>
:root{
  --leaf:#9cc43a;
  --bark:#6b4a1e;
  --bark-soft:#8a6a3a;
  --sky:#dfe3ee;
  --field:#cfd3a6;
  --paper:#ffffff;
  --ink:#3a2a12;
  --canvas:#ffffff;
  --field-line:#e9ebf0;
}
*{box-sizing:border-box;margin:0;padding:0}
html,body{width:789px;height:1200px;overflow:hidden;background:var(--canvas)}
body{position:relative;font-family:"PT Sans",sans-serif;color:var(--bark)}

/* presentation grid */
.screen{position:absolute;left:214px;top:87px;width:355px;height:222px;overflow:hidden;box-shadow:0 6px 18px rgba(0,0,0,.12)}
.screen .page{transform:scale(1.4257);transform-origin:0 0;box-shadow:none}
.page{position:absolute;width:249px;height:319px;overflow:hidden;background:var(--paper);box-shadow:0 1px 4px rgba(0,0,0,.15)}
.page--home{left:96px;top:419px}
.page--saddles{left:443px;top:419px}
.page--prices{left:96px;top:813px}
.page--contact{left:443px;top:813px}

/* shared site chrome */
.backdrop{position:absolute;left:0;top:22px;width:249px;height:263px;background:linear-gradient(180deg,var(--sky) 0%,var(--sky) 55%,#d3d8c4 75%,var(--field) 100%)}
.site-head{position:absolute;left:0;top:0;width:249px;height:22px;background:var(--paper)}
.accent-band{position:absolute;left:80px;top:0;width:90px;height:5px}
.head-mail{position:absolute;left:169px;top:3px;font-size:3.2px;font-weight:700;color:var(--leaf)}
.brand{position:absolute;display:flex;align-items:center;gap:1.5px;white-space:nowrap}
.brand-dot{width:4px;height:4px;border-radius:50%;background:var(--leaf)}
.brand-name{font-size:4px;color:var(--bark-soft);letter-spacing:.2px;text-transform:uppercase}
.site-head .brand{left:50px;top:14px}
.site-nav{position:absolute;top:16px;left:130px;display:flex;gap:13px;font-size:3.2px;color:var(--ink)}
.site-foot{position:absolute;left:0;top:285px;width:249px;height:34px;background:var(--paper);text-align:center}
.site-foot .brand{left:50%;top:8px;transform:translateX(-50%)}
.site-foot .brand-name{font-size:2.6px}
.site-foot .brand-dot{width:2.6px;height:2.6px}
.foot-line{position:absolute;left:0;width:100%;font-size:2.8px;font-weight:700;color:var(--ink)}
.foot-line--addr{top:22px}
.foot-line--links{top:27px;font-size:2.2px}

.panel{position:absolute;background:var(--paper)}
.page-title{position:absolute;left:51px;top:31px;font-size:4.6px;font-weight:700;color:var(--ink)}
.photo{position:absolute}

/* home */
.hero{position:absolute;left:0;top:22px;width:249px;height:88px;background:linear-gradient(100deg,#6b4a2e 0%,#b5582a 35%,#c9662f 55%,#8d8a7a 75%,#4a3a2c 100%)}
.hero-claim{position:absolute;left:96px;top:44px;width:130px;text-align:center;font-family:"Open Sans",sans-serif;color:#fff;line-height:1.2}
.hero-claim strong{display:block;font-size:4.6px}
.hero-claim span{display:block;font-size:4.2px}
.home-panel{left:48px;top:115px;width:152px;height:164px}
.home-panel .brand{left:50%;top:12px;transform:translateX(-50%)}
.teaser-img{left:32px;width:37px;height:25px}
.teaser-text{position:absolute;left:76px;width:52px;font-size:2.2px;line-height:1.35;color:var(--bark)}
.teaser-text b{display:block;color:var(--ink)}

/* saddles */
.saddle-panel{left:49px;top:41px;width:152px;height:238px}
.saddle-card{position:absolute;width:40px}
.saddle-card .photo{position:static;display:block;width:36px;height:35px;background:linear-gradient(135deg,#f2f2f2,#3a3330 55%,#1f1b19)}
.saddle-card dl{margin-top:4px;font-size:2.1px;line-height:1.35;color:var(--bark)}
.saddle-card dt{font-weight:700}
.saddle-card a{color:var(--bark);text-decoration:underline}

/* prices */
.price-panel{left:48px;top:40px;width:152px;height:240px}
.price-panel .brand{left:64px;top:26px}
.price-panel .brand-name{font-size:5.4px}
.price-panel .brand-dot{width:5px;height:5px}
.price-head{position:absolute;left:5px;font-size:2.6px;font-weight:700;color:var(--ink)}
.price-list{position:absolute;width:36px;font-size:2.1px;line-height:1.35;color:var(--bark)}
.price-list li{list-style:none;display:flex;justify-content:space-between}
.price-copy{position:absolute;top:164px;width:66px;font-size:2.5px;line-height:1.3;color:var(--bark)}

/* contact */
.contact-panel{left:49px;top:44px;width:152px;height:238px}
.contact-lead{position:absolute;left:3px;top:4px;font-size:2.4px;font-weight:700;color:var(--ink)}
.field{position:absolute;left:3px;width:68px;height:6px;background:var(--field-line);font-size:2.2px;color:#8a8f98;padding:1.6px 2px}
.field--message{width:146px;height:52px}
.contact-address{position:absolute;left:82px;top:12px;font-size:2.4px;line-height:1.35;color:var(--bark);font-style:normal}
.check{position:absolute;left:3px;display:flex;align-items:center;gap:3px;font-size:2.2px;color:#6a6f78}
.check i{width:3px;height:3px;border:.3px solid #bbb;display:block}
.send-btn{position:absolute;left:61px;top:113px;width:30px;height:8px;background:var(--leaf);color:#fff;font-size:3.6px;font-weight:700;text-align:center;line-height:8px}
.map{left:5px;top:140px;width:146px;height:92px;background:linear-gradient(135deg,#eef0e8,#dfe8d2 50%,#e9ede2)}
</style>
</head>
<body>

<!-- home page, large -->
<div class="screen">
  <section class="page">
    <div class="backdrop" role="img" aria-label="Hintergrundfoto: heller Himmel über einem Feld"></div>
    <header class="site-head">
      <svg class="accent-band" viewBox="0 0 90 5" aria-hidden="true"><polygon points="0,0 90,0 87,5 4,5" fill="var(--leaf)"/></svg>
      <span class="head-mail">lena@oakrein-saettel.de</span>
      <div class="brand"><span class="brand-dot"></span><span class="brand-name">Oakrein Sättel</span></div>
      <nav class="site-nav"><span>Home</span><span>Sättel</span><span>Preise</span><span>Kontakt</span></nav>
    </header>
    <div class="hero" role="img" aria-label="Foto: zwei Pferde auf einem Turnierplatz, Reiterin im Sattel"></div>
    <p class="hero-claim"><strong>Gebrauchte Markensättel</strong><span>in allerbester Qualität</span></p>
    <div class="panel home-panel">
      <div class="brand"><span class="brand-dot"></span><span class="brand-name">Oakrein Sättel</span></div>
    </div>
  </section>
</div>

<!-- home page -->
<section class="page page--home">
  <div class="backdrop" role="img" aria-label="Hintergrundfoto: Rapsfeld unter hellem Himmel"></div>
  <header class="site-head">
    <svg class="accent-band" viewBox="0 0 90 5" aria-hidden="true"><polygon points="0,0 90,0 87,5 4,5" fill="var(--leaf)"/></svg>
    <span class="head-mail">lena@oakrein-saettel.de</span>
    <div class="brand"><span class="brand-dot"></span><span class="brand-name">Oakrein Sättel</span></div>
    <nav class="site-nav"><span>Home</span><span>Sättel</span><span>Preise</span><span>Kontakt</span></nav>
  </header>
  <div class="hero" role="img" aria-label="Foto: zwei Pferde auf einem Turnierplatz, Reiterin im Sattel"></div>
  <p class="hero-claim"><strong>Gebrauchte Markensättel</strong><span>in allerbester Qualität</span></p>
  <div class="panel home-panel">
    <div class="brand"><span class="brand-dot"></span><span class="brand-name">Oakrein Sättel</span></div>
    <div class="photo teaser-img" style="top:48px;background:linear-gradient(135deg,#6a7a4a,#3b2a1e)" role="img" aria-label="Foto: Sattel auf einem Sattelbock im Grünen"></div>
    <p class="teaser-text" style="top:49px">Du suchst einen hochwertigen Gebrauchtsattel? Bei uns findest du ständig über hundert geprüfte Sättel aller Marken und Preisklassen. Außerdem bieten wir Ankauf und Kommission an.</p>
    <div class="photo teaser-img" style="top:85px;background:#f1f1f3;border:.4px solid #ccc" role="img" aria-label="Platzhalter für ein Teamfoto"></div>
    <p class="teaser-text" style="top:86px"><b>Das Oakrein-Team</b>Wir reiten selbst seit vielen Jahren und beraten dich gern persönlich bei der Auswahl des passenden Sattels.</p>
    <div class="photo teaser-img" style="top:119px;background:linear-gradient(135deg,#8a4a2a,#2e2624)" role="img" aria-label="Foto: Sattel auf einem Pferderücken"></div>
    <p class="teaser-text" style="top:120px"><b>Sattelanprobe</b>Wir kommen mit passenden Sätteln zu dir in den Stall und prüfen den Sitz direkt am Pferd vor Ort.</p>
  </div>
  <footer class="site-foot">
    <div class="brand"><span class="brand-dot"></span><span class="brand-name">Oakrein Sättel</span></div>
    <p class="foot-line foot-line--addr">Oakrein Sättel | Lena Marquardt | Gut am Wiesenrand | 12345 Musterdorf | lena@oakrein-saettel.de</p>
    <p class="foot-line foot-line--links">Kontakt | Impressum | Datenschutzerklärung | Widerrufsbelehrung</p>
  </footer>
</section>

<!-- saddle listing -->
<section class="page page--saddles">
  <div class="backdrop" role="img" aria-label="Hintergrundfoto: Rapsfeld unter hellem Himmel"></div>
  <header class="site-head">
    <svg class="accent-band" viewBox="0 0 90 5" aria-hidden="true"><polygon points="0,0 90,0 87,5 4,5" fill="var(--leaf)"/></svg>
    <span class="head-mail">lena@oakrein-saettel.de</span>
    <div class="brand"><span class="brand-dot"></span><span class="brand-name">Oakrein Sättel</span></div>
    <nav class="site-nav"><span>Home</span><span>Sättel</span><span>Preise</span><span>Kontakt</span></nav>
  </header>
  <h2 class="page-title">Sattelauswahl</h2>
  <div class="panel saddle-panel">
    <article class="saddle-card" style="left:4px;top:3px"><div class="photo" role="img" aria-label="Produktfoto: schwarzer Dressursattel"></div><dl><dt>Satteltyp &amp; Marke</dt><dd>Sitzfläche: XX Zoll</dd><dd>Sattelblatt: normal</dd><dd>Kammerweite: XXX</dd><dd>Baujahr: XXXX</dd><dd>Farbe: XXXXX</dd><dd><a>mehr erfahren</a></dd></dl></article>
    <article class="saddle-card" style="left:58px;top:3px"><div class="photo" role="img" aria-label="Produktfoto: brauner Dressursattel"></div><dl><dt>Satteltyp &amp; Marke</dt><dd>Sitzfläche: XX Zoll</dd><dd>Sattelblatt: normal</dd><dd>Kammerweite: XXX</dd><dd>Baujahr: XXXX</dd><dd>Farbe: XXXXX</dd><dd><a>mehr erfahren</a></dd></dl></article>
    <article class="saddle-card" style="left:111px;top:3px"><div class="photo" role="img" aria-label="Produktfoto: schwarzer Dressursattel"></div><dl><dt>Satteltyp &amp; Marke</dt><dd>Sitzfläche: XX Zoll</dd><dd>Sattelblatt: normal</dd><dd>Kammerweite: XXX</dd><dd>Baujahr: XXXX</dd><dd>Farbe: XXXXX</dd><dd><a>mehr erfahren</a></dd></dl></article>
    <article class="saddle-card" style="left:4px;top:83px"><div class="photo" role="img" aria-label="Produktfoto: schwarzer Dressursattel"></div><dl><dt>Satteltyp &amp; Marke</dt><dd>Sitzfläche: XX Zoll</dd><dd>Sattelblatt: normal</dd><dd>Kammerweite: XXX</dd><dd>Baujahr: XXXX</dd><dd>Farbe: XXXXX</dd><dd><a>mehr erfahren</a></dd></dl></article>
    <article class="saddle-card" style="left:58px;top:83px"><div class="photo" role="img" aria-label="Produktfoto: brauner Dressursattel"></div><dl><dt>Satteltyp &amp; Marke</dt><dd>Sitzfläche: XX Zoll</dd><dd>Sattelblatt: normal</dd><dd>Kammerweite: XXX</dd><dd>Baujahr: XXXX</dd><dd>Farbe: XXXXX</dd><dd><a>mehr erfahren</a></dd></dl></article>
    <article class="saddle-card" style="left:111px;top:83px"><div class="photo" role="img" aria-label="Produktfoto: schwarzer Dressursattel"></div><dl><dt>Satteltyp &amp; Marke</dt><dd>Sitzfläche: XX Zoll</dd><dd>Sattelblatt: normal</dd><dd>Kammerweite: XXX</dd><dd>Baujahr: XXXX</dd><dd>Farbe: XXXXX</dd><dd><a>mehr erfahren</a></dd></dl></article>
    <article class="saddle-card" style="left:4px;top:166px"><div class="photo" role="img" aria-label="Produktfoto: schwarzer Dressursattel"></div><dl><dt>Satteltyp &amp; Marke</dt><dd>Sitzfläche: XX Zoll</dd><dd>Sattelblatt: normal</dd><dd>Kammerweite: XXX</dd><dd>Baujahr: XXXX</dd><dd>Farbe: XXXXX</dd><dd><a>mehr erfahren</a></dd></dl></article>
    <article class="saddle-card" style="left:58px;top:166px"><div class="photo" role="img" aria-label="Produktfoto: brauner Dressursattel"></div><dl><dt>Satteltyp &amp; Marke</dt><dd>Sitzfläche: XX Zoll</dd><dd>Sattelblatt: normal</dd><dd>Kammerweite: XXX</dd><dd>Baujahr: XXXX</dd><dd>Farbe: XXXXX</dd><dd><a>mehr erfahren</a></dd></dl></article>
    <article class="saddle-card" style="left:111px;top:166px"><div class="photo" role="img" aria-label="Produktfoto: schwarzer Dressursattel"></div><dl><dt>Satteltyp &amp; Marke</dt><dd>Sitzfläche: XX Zoll</dd><dd>Sattelblatt: normal</dd><dd>Kammerweite: XXX</dd><dd>Baujahr: XXXX</dd><dd>Farbe: XXXXX</dd><dd><a>mehr erfahren</a></dd></dl></article>
  </div>
  <footer class="site-foot">
    <div class="brand"><span class="brand-dot"></span><span class="brand-name">Oakrein Sättel</span></div>
    <p class="foot-line foot-line--addr">Oakrein Sättel | Lena Marquardt | Gut am Wiesenrand | 12345 Musterdorf | lena@oakrein-saettel.de</p>
    <p class="foot-line foot-line--links">Kontakt | Impressum | Datenschutzerklärung | Widerrufsbelehrung</p>
  </footer>
</section>

<!-- price list -->
<section class="page page--prices">
  <div class="backdrop" role="img" aria-label="Hintergrundfoto: Rapsfeld unter hellem Himmel"></div>
  <header class="site-head">
    <svg class="accent-band" viewBox="0 0 90 5" aria-hidden="true"><polygon points="0,0 90,0 87,5 4,5" fill="var(--leaf)"/></svg>
    <span class="head-mail">lena@oakrein-saettel.de</span>
    <div class="brand"><span class="brand-dot"></span><span class="brand-name">Oakrein Sättel</span></div>
    <nav class="site-nav"><span>Home</span><span>Sättel</span><span>Preise</span><span>Kontakt</span></nav>
  </header>
  <h2 class="page-title">Preisliste</h2>
  <div class="panel price-panel">
    <h3 class="price-head" style="top:10px">Sattelanprobe</h3>
    <ul class="price-list" style="left:5px;top:17px;width:26px"><li><span>Je Stunde:</span><span>XXX €</span></li><li><span>Anfahrt je km:</span><span>XXX €</span></li></ul>
    <ul class="price-list" style="left:5px;top:28px;width:26px"><li><span>Selbstabholer:</span><span>XXX €</span></li><li><span>Testwochen:</span><span>XXX €</span></li></ul>
    <div class="brand"><span class="brand-dot"></span><span class="brand-name">Oakrein Sättel</span></div>
    <h3 class="price-head" style="top:50px">Sattelpreise</h3>
    <ul class="price-list" style="left:5px;top:58px"><li><span>Dressur</span><span>XXX €</span></li><li><span>Springen</span><span>XXX €</span></li><li><span>Vielseitig</span><span>XXX €</span></li><li><span>Gelände</span><span>XXX €</span></li><li><span>Western</span><span>XXX €</span></li><li><span>Pony</span><span>XXX €</span></li><li><span>Kinder</span><span>XXX €</span></li><li><span>Kommission</span><span>XXX €</span></li><li><span>Ankauf</span><span>XXX €</span></li><li><span>Reinigung</span><span>XXX €</span></li><li><span>Polster</span><span>XXX €</span></li><li><span>Gurt</span><span>XXX €</span></li></ul>
    <ul class="price-list" style="left:58px;top:58px"><li><span>Dressur</span><span>XXX €</span></li><li><span>Springen</span><span>XXX €</span></li><li><span>Vielseitig</span><span>XXX €</span></li><li><span>Gelände</span><span>XXX €</span></li><li><span>Western</span><span>XXX €</span></li><li><span>Pony</span><span>XXX €</span></li><li><span>Kinder</span><span>XXX €</span></li><li><span>Kommission</span><span>XXX €</span></li><li><span>Ankauf</span><span>XXX €</span></li><li><span>Reinigung</span><span>XXX €</span></li><li><span>Polster</span><span>XXX €</span></li><li><span>Gurt</span><span>XXX €</span></li></ul>
    <ul class="price-list" style="left:111px;top:58px"><li><span>Dressur</span><span>XXX €</span></li><li><span>Springen</span><span>XXX €</span></li><li><span>Vielseitig</span><span>XXX €</span></li><li><span>Gelände</span><span>XXX €</span></li><li><span>Western</span><span>XXX €</span></li><li><span>Pony</span><span>XXX €</span></li><li><span>Kinder</span><span>XXX €</span></li><li><span>Kommission</span><span>XXX €</span></li><li><span>Ankauf</span><span>XXX €</span></li><li><span>Reinigung</span><span>XXX €</span></li><li><span>Polster</span><span>XXX €</span></li><li><span>Gurt</span><span>XXX €</span></li></ul>
    <ul class="price-list" style="left:5px;top:112px"><li><span>Steigbügel</span><span>XXX €</span></li><li><span>Leder</span><span>XXX €</span></li><li><span>Schabracke</span><span>XXX €</span></li><li><span>Pad</span><span>XXX €</span></li><li><span>Trense</span><span>XXX €</span></li><li><span>Zügel</span><span>XXX €</span></li><li><span>Decke</span><span>XXX €</span></li><li><span>Halfter</span><span>XXX €</span></li><li><span>Pflege</span><span>XXX €</span></li><li><span>Versand</span><span>XXX €</span></li><li><span>Sonstiges</span><span>XXX €</span></li></ul>
    <div class="photo" style="left:58px;top:109px;width:83px;height:41px;background:linear-gradient(135deg,#8fa07a,#6a4a34 55%,#3a2a20)" role="img" aria-label="Foto: gesatteltes Pferd vor einem Stallgebäude"></div>
    <p class="price-copy" style="left:5px">Alle Sättel werden vor dem Verkauf gründlich gereinigt, gepflegt und auf Schäden geprüft. Auf Wunsch passen wir die Kammerweite an und bringen den Sattel zur Anprobe direkt zu dir in den Stall. Bei Fragen zu Preisen oder Zahlung melde dich gern jederzeit.</p>
    <p class="price-copy" style="left:76px">Gebrauchte Sättel kaufen wir nach Prüfung an oder nehmen sie in Kommission. Der Preis richtet sich nach Marke, Zustand und Alter. Wir fotografieren jeden Sattel, stellen ihn online und kümmern uns um Beratung und Versand, damit du entspannt verkaufen kannst.</p>
  </div>
  <footer class="site-foot">
    <div class="brand"><span class="brand-dot"></span><span class="brand-name">Oakrein Sättel</span></div>
    <p class="foot-line foot-line--addr">Oakrein Sättel | Lena Marquardt | Gut am Wiesenrand | 12345 Musterdorf | lena@oakrein-saettel.de</p>
    <p class="foot-line foot-line--links">Kontakt | Impressum | Datenschutzerklärung | Widerrufsbelehrung</p>
  </footer>
</section>

<!-- contact -->
<section class="page page--contact">
  <div class="backdrop" role="img" aria-label="Hintergrundfoto: Rapsfeld unter hellem Himmel"></div>
  <header class="site-head">
    <svg class="accent-band" viewBox="0 0 90 5" aria-hidden="true"><polygon points="0,0 90,0 87,5 4,5" fill="var(--leaf)"/></svg>
    <span class="head-mail">lena@oakrein-saettel.de</span>
    <div class="brand"><span class="brand-dot"></span><span class="brand-name">Oakrein Sättel</span></div>
    <nav class="site-nav"><span>Home</span><span>Sättel</span><span>Preise</span><span>Kontakt</span></nav>
  </header>
  <h2 class="page-title">Kontakt</h2>
  <div class="panel contact-panel">
    <p class="contact-lead">Du hast weitere Fragen? Dann stell Sie uns gerne hier im Kontaktformular</p>
    <div class="field" style="top:13px">Name</div>
    <div class="field" style="top:23px">Email Adresse</div>
    <div class="field" style="top:34px">Betreff</div>
    <address class="contact-address">Oakrein Sättel<br>Lena Marquardt<br>Gut am Wiesenrand<br>12345 Musterdorf<br><br>0170 1234567<br>lena@oakrein-saettel.de</address>
    <div class="field field--message" style="top:45px">Nachricht</div>
    <label class="check" style="top:100px"><i></i>Kopie an mich senden</label>
    <label class="check" style="top:107px"><i></i>Hiermit bestätige ich, dass ich die Datenschutzerklärung gelesen habe und ihr zustimme</label>
    <div class="send-btn">Absenden</div>
    <div class="photo map" role="img" aria-label="Karte mit dem Standort des Hofes"></div>
  </div>
  <footer class="site-foot">
    <div class="brand"><span class="brand-dot"></span><span class="brand-name">Oakrein Sättel</span></div>
    <p class="foot-line foot-line--addr">Oakrein Sättel | Lena Marquardt | Gut am Wiesenrand | 12345 Musterdorf | lena@oakrein-saettel.de</p>
    <p class="foot-line foot-line--links">Kontakt | Impressum | Datenschutzerklärung | Widerrufsbelehrung</p>
  </footer>
</section>

</body>
</html>
```